Website Design for Nubelo Cloud As a Service

We are building a service to allow customers to own their own private clouds easily and cheaply. Owning your own private cloud saves costs, and offers more flexibility than a public cloud provider but has historically been a complex and expensive option.

We plan to offer a service where we build and maintain your own private cloud on your own hardware for a cheap monthly costs. Similar to this service - https://stackorra.com/solutions/private-cloud

We already have a logo and branding in place - we'd like a website design to be tailored from this branding, see attached logo design.

Feel free to add important elements on the home page such as testimonials, client/partner logos, contact form, social media, etc using placeholder contents in addition to the document we attached.

We also plan to add sub-pages in the future so please make sure that your website design has a full navigation menu.

An example of the site we like: https://www.verimoxa.com/ we'd be happy for you to take inspiration from this website.

Target Market(s)

B2B focused, we are targeting start-up/small/medium sized companies who needs help with their cloud and IT infrastructure.

Industry/Entity Type

IT

Number of Pages Required

1 page

Font styles to use
Other font styles liked:
• Please refer to the attachment - font must have Mayeka Demi Bold & Retroica

Requirements
Must have
• Please add placeholder menu since we're planning to have subpages later on.

```html
<!DOCTYPE html>
<html lang="en">
<head>
<meta charset="utf-8">
<title>Nubelo Cloud as a Service</title>
<link href="https://fonts.googleapis.com/css2?family=Montserrat:wght@500;600;700&family=Montserrat+Alternates:wght@400;500;600&display=swap" rel="stylesheet">
<style>
:root{
  --blue:#1a76cc;
  --blue-dark:#0f4f91;
  --navy:#0b1624;
  --ink:#333a44;
  --muted:#7b8189;
  --line:#e2e6ea;
  --white:#fff;
  --footer:#2b2f34;
}
*{box-sizing:border-box;margin:0;padding:0}
html,body{width:1200px;height:4367px;overflow:hidden}
body{font-family:"Montserrat Alternates",sans-serif;color:var(--ink);background:var(--white);position:relative}
h1,h2,h3,h4{font-family:"Montserrat",sans-serif}
.abs{position:absolute}
/* top bar */
.topbar{position:absolute;top:0;left:0;width:1200px;height:42px;background:var(--ink);background:#2e3033;color:#fff;font-size:13px;display:flex;align-items:center;padding:0 110px}
.topbar .sep{margin:0 14px}
.topbar .ico{color:#4aa3ff;margin-right:6px}
.social{display:flex;gap:8px;margin-left:auto}
.social span{width:34px;height:34px;border-radius:50%;background:#fff;display:block}
.social span:first-child{background:var(--blue)}
/* header */
.header{position:absolute;top:42px;left:0;width:1200px;height:76px;background:#fff;display:flex;align-items:center;padding:0 110px;box-shadow:0 2px 6px rgba(0,0,0,.06)}
.brand{display:flex;align-items:center;gap:10px;font-family:"Montserrat",sans-serif;font-weight:600;font-size:30px;color:var(--blue)}
.brand i{width:34px;height:34px;border-radius:50%;background:var(--blue);display:block}
.nav{margin-left:auto;display:flex;gap:32px;font-size:13px;font-family:"Montserrat",sans-serif;font-weight:500;color:#444}
.nav a{color:inherit;text-decoration:none}
.nav a.active{color:var(--blue)}
/* hero */
.hero{position:absolute;top:118px;left:0;width:1200px;height:601px;background:linear-gradient(120deg,#1f6fb6,#1560a8 55%,#0c3f78);overflow:hidden}
.hero-photo{position:absolute;right:0;top:0;width:720px;height:601px;clip-path:polygon(48% 0,100% 0,100% 100%,0 100%);background:radial-gradient(circle at 70% 40%,#f0a860 0,#9a5a3a 18%,#1d3a5e 48%,#0b1f36 100%)}
.hero-copy{position:absolute;left:112px;top:160px;width:460px;color:#fff}
.hero-copy h1{font-size:27px;line-height:1.35;font-weight:600;border-left:3px solid #fff;padding-left:22px;margin-left:22px}
.hero-copy p{font-size:14.5px;line-height:1.8;margin-top:22px}
.btn{display:inline-block;border-radius:30px;font-family:"Montserrat",sans-serif;font-weight:600;font-size:14px;text-align:center}
.btn-white{background:#fff;color:#333;padding:14px 24px;margin-top:24px}
.btn-blue{background:var(--blue);color:#fff}
.dots{position:absolute;left:112px;top:562px;display:flex;gap:7px}
.dots span{width:13px;height:13px;border:2px solid #fff;border-radius:50%}
.dots span.on{background:#fff}
/* section titles */
.title{text-align:center;font-size:31px;font-weight:600;line-height:1.3;color:#444}
/* benefits */
.cards{position:absolute;left:112px;width:975px;display:grid;grid-template-columns:repeat(3,307px);gap:27px 27px}
.card{height:248px;background:#fff;border-radius:8px;box-shadow:0 4px 16px rgba(0,0,0,.12);text-align:center;padding:28px 20px}
.card.featured{background:var(--blue);color:#fff}
.card .icon{width:88px;height:88px;border-radius:50%;background:var(--blue);margin:0 auto;display:flex;align-items:center;justify-content:center}
.card.featured .icon{background:#fff}
.card h3{font-size:16px;font-weight:700;margin-top:26px;color:#444;letter-spacing:.3px}
.card.featured h3{color:#fff}
.card p{font-size:13.5px;line-height:1.75;margin-top:14px;color:var(--muted)}
.card.featured p{color:#fff}
/* dark */
.dark{position:absolute;top:1542px;left:0;width:1200px;height:624px;background:radial-gradient(ellipse at 60% 50%,#1e2a3a,#070b12 75%);color:#fff;text-align:center}
.dark h2{font-size:31px;font-weight:600;line-height:1.3;margin-top:50px}
.dark p{font-size:13.5px;line-height:1.75;width:960px;margin:0 auto}
.steps{position:absolute;top:340px;left:0;width:1200px;height:200px}
.step{position:absolute;width:160px;text-align:center;margin-left:-80px}
.step .c{width:92px;height:92px;border-radius:50%;background:#fff;margin:0 auto;display:flex;align-items:center;justify-content:center}
.step b{display:block;font-family:"Montserrat",sans-serif;font-size:19px;font-weight:600;margin-top:20px}
/* difference */
.diff-photo{position:absolute;top:2166px;left:0;width:642px;height:566px;background:radial-gradient(circle at 55% 45%,#c47a4a 0,#5a3b30 25%,#1b2533 60%,#0e141c 100%)}
.dotgrid{position:absolute;top:2738px;left:462px;width:112px;height:44px;background-image:radial-gradient(#c9ccd1 1.6px,transparent 1.8px);background-size:11px 11px}
.diff-card{position:absolute;top:2246px;left:575px;width:512px;height:559px;background:#fff;box-shadow:0 4px 20px rgba(0,0,0,.12);padding:44px 36px}
.diff-card h2{font-size:28px;font-weight:600;color:#444}
.diff-card ul{list-style:none;margin-top:30px}
.diff-card li{position:relative;padding-left:35px;font-size:13px;line-height:1.75;color:var(--muted);margin-bottom:15px}
.diff-card li::before{content:"";position:absolute;left:0;top:5px;width:12px;height:12px;border:2px solid var(--blue);border-radius:50%}
.diff-card li::after{content:"";position:absolute;left:5px;top:10px;width:4px;height:4px;background:var(--blue);border-radius:50%}
/* blue section */
.bluezone{position:absolute;top:2886px;left:0;width:1200px;height:611px;background:linear-gradient(180deg,#1f7ed6,#1567b8)}
.bluezone .title{color:#fff;margin-top:80px}
.bcards{position:absolute;top:194px;left:112px;display:grid;grid-template-columns:repeat(3,307px);gap:27px}
.bcard{height:340px;background:#fff;text-align:center;padding:28px 22px}
.bcard .ring{width:94px;height:94px;border-radius:50%;border:4px solid var(--blue);margin:0 auto;display:flex;align-items:center;justify-content:center}
.bcard h3{font-size:16px;font-weight:600;line-height:1.6;color:#444;margin-top:24px}
.bcard p{font-size:12.5px;line-height:1.85;color:var(--muted);margin-top:14px}
/* contact */
.contact{position:absolute;top:3497px;left:0;width:1200px;height:554px}
.contact .title{margin-top:72px}
.info{position:absolute;top:150px;display:flex;gap:18px}
.info .pin{width:66px;height:66px;border-radius:50%;box-shadow:0 3px 12px rgba(0,0,0,.12);display:flex;align-items:center;justify-content:center;flex:none}
.info h4{font-size:14px;font-weight:600;color:#444;margin-top:6px}
.info p{font-size:13px;color:var(--muted);line-height:1.6;margin-top:8px}
.field{position:absolute;height:48px;border:1px solid var(--line);background:#fff;box-shadow:0 2px 6px rgba(0,0,0,.05);font-size:13px;color:#555;padding:15px 18px}
.send{position:absolute;top:412px;left:511px;width:178px;height:50px;line-height:50px}
/* footer */
.footer{position:absolute;top:4051px;left:0;width:1200px;height:316px;background:var(--footer);color:#fff;text-align:center}
.footer .brand{justify-content:center;margin-top:40px;color:#fff}
.footer .brand em{font-style:normal}
.fnav{margin-top:42px;font-family:"Montserrat",sans-serif;font-weight:600;font-size:17px}
.fnav span{margin:0 14px}
.fcontact{margin-top:22px;font-size:16px}
.fsocial{display:flex;gap:8px;justify-content:center;margin-top:20px}
.fsocial span{width:34px;height:34px;border-radius:50%;background:#fff}
.fsocial span:first-child{background:var(--blue)}
.copy{position:absolute;bottom:0;left:112px;width:976px;border-top:1px solid #555;padding:14px 0;font-size:12px}
</style>
</head>
<body>

<div class="topbar">
  <span class="ico">&#9742;</span>+1 (888) 888 8888<span class="sep">|</span><span class="ico">&#9993;</span>info@nubelocloud.com
  <div class="social"><span></span><span></span><span></span><span></span></div>
</div>

<header class="header">
  <div class="brand"><i></i>NubeloCloud</div>
  <nav class="nav">
    <a class="active" href="#">HOME</a><a href="#">ABOUT US</a><a href="#">PRODUCTS</a><a href="#">SOLUTIONS</a><a href="#">RESOURCES</a><a href="#">CONTACT US</a>
  </nav>
</header>

<section class="hero">
  <div class="hero-photo" role="img" aria-label="Hands typing on a laptop with glowing cloud network graphics"></div>
  <div class="hero-copy">
    <h1>A groundbreaking way for your small business to benefit from the power of the cloud</h1>
    <p>Nubelo Cloud as a Service is here to help small businesses utilise the power of the cloud without complicated set-ups or scary price tags</p>
    <span class="btn btn-white">CONTACT US</span>
  </div>
  <div class="dots"><span></span><span class="on"></span><span></span><span></span></div>
</section>

<h2 class="title abs" style="top:800px;left:0;width:1200px">How NCAAS benefits<br>your business</h2>

<div class="cards" style="top:924px">
  <div class="card"><div class="icon"><svg width="44" height="44" viewBox="0 0 44 44" fill="none" stroke="#fff" stroke-width="2.5"><path d="M10 28a8 8 0 0 1 2-15 11 11 0 0 1 21 3 7 7 0 0 1-1 12z"/></svg></div><h3>TOTALLY FLEXIBLE</h3><p>Get the cloud you want and the latest innovations you need</p></div>
  <div class="card featured"><div class="icon"><svg width="44" height="44" viewBox="0 0 44 44" fill="none" stroke="#1a76cc" stroke-width="2.5"><circle cx="24" cy="24" r="13"/><path d="M24 16v8l5 4M20 6h8M4 20h8M6 26h6"/></svg></div><h3>FASTER</h3><p>Our private cloud solutions outpace public clouds</p></div>
  <div class="card"><div class="icon"><svg width="44" height="44" viewBox="0 0 44 44" fill="none" stroke="#fff" stroke-width="2.5"><path d="M8 16l6-8h16l6 8-14 20z M8 16h28"/></svg></div><h3>GREATER VALUE</h3><p>Totally transparent pricing for no nasty month-end surprises</p></div>
  <div class="card"><div class="icon"><svg width="44" height="44" viewBox="0 0 44 44" fill="none" stroke="#fff" stroke-width="2.5"><circle cx="22" cy="22" r="14"/><path d="M12 12l20 20"/></svg></div><h3>NO CONSULTANCY FEES</h3><p>We'll work with you and charge set fees for everything</p></div>
  <div class="card"><div class="icon"><svg width="44" height="44" viewBox="0 0 44 44" fill="none" stroke="#fff" stroke-width="2.5"><circle cx="22" cy="16" r="6"/><path d="M10 36c0-7 5-11 12-11s12 4 12 11"/></svg></div><h3>MANAGEMENT</h3><p>They're all included in your monthly price</p></div>
  <div class="card"><div class="icon"><svg width="44" height="44" viewBox="0 0 44 44" fill="none" stroke="#fff" stroke-width="2.5"><path d="M10 26a7 7 0 0 1 2-13 10 10 0 0 1 19 3 6 6 0 0 1-1 10zM22 26v10M14 36h16"/></svg></div><h3>CLOUD SOLUTIONS</h3><p>We'll deploy the right OpenStratum solutions for your business</p></div>
</div>

<section class="dark">
  <h2>NCAAS can drive your digital<br>transformation today</h2>
  <p style="margin-top:36px">Organisations of all shapes and sizes are reaping the time and money saving benefits that the cloud brings. But for small businesses seeking to transition, managing the time and financial costs of transitioning, and knowing whether to opt for a public or private cloud can cause you to hit the pause button.</p>
  <p style="margin-top:22px">NCAAS is here to help you switch on your cloud transformation in a way that works best for you. We deliver and support fully managed private cloud solutions that are:</p>
  <div class="steps">
    <svg class="abs" style="left:0;top:0" width="1200" height="140" fill="none" stroke="#fff" stroke-width="3" stroke-dasharray="12 9"><path d="M300 50 C340 110 450 110 500 60 C560 -10 650 0 698 50 C760 100 840 40 898 40"/></svg>
    <div class="step" style="left:300px"><div class="c"><svg width="44" height="44" viewBox="0 0 44 44" fill="none" stroke="#1a76cc" stroke-width="3"><circle cx="24" cy="25" r="12"/><path d="M24 25l5-5M20 8h8"/></svg></div><b>FAST</b></div>
    <div class="step" style="left:500px"><div class="c"><svg width="44" height="44" viewBox="0 0 44 44" fill="#1a76cc"><path d="M14 20h4V8a3 3 0 0 1 6 0v10l8 2c3 1 4 3 3 6l-3 10H18l-6-10z"/></svg></div><b>EASY</b></div>
    <div class="step" style="left:698px"><div class="c"><svg width="44" height="44" viewBox="0 0 44 44"><circle cx="22" cy="22" r="16" fill="none" stroke="#1a76cc" stroke-width="3"/><path d="M24 10l-9 14h7l-2 10 9-14h-7z" fill="#1a76cc"/></svg></div><b>POWERFUL</b></div>
    <div class="step" style="left:898px"><div class="c"><svg width="44" height="44" viewBox="0 0 44 44" fill="none" stroke="#1a76cc" stroke-width="3"><rect x="8" y="8" width="28" height="28" rx="2"/><path d="M16 28l12-12M20 16h8v8"/></svg></div><b>SCALABLE</b></div>
  </div>
  <span class="btn btn-blue abs" style="left:523px;top:518px;width:154px;height:46px;line-height:46px">GET STARTED</span>
</section>

<div class="diff-photo" role="img" aria-label="Hands on a laptop keyboard beneath a glowing cloud linked to security, device and data icons"></div>
<div class="dotgrid"></div>
<div class="diff-card">
  <h2>The NCAAS Difference</h2>
  <ul>
    <li>We'll quickly get to grips with what your organisation needs, and deliver it via our private cloud solutions</li>
    <li>Enjoy the ease of the public cloud, combined with the features, innovations and flexibility of the private cloud</li>
    <li>You can focus on your core business while we support you with a dedicated cloud infrastructure</li>
    <li>We'll create and deliver the launchpad that will take your business forward</li>
    <li>Get the benefits of your own cloud infrastructure and reduce your operational costs</li>
    <li>Fast &amp; easy computing, storage and network resources</li>
    <li>Managed operations from private OpenStratum clouds and Podweave</li>
    <li>We'll support your growth and scale your cloud as you need it</li>
  </ul>
</div>

<section class="bluezone">
  <h2 class="title">How NCAAS benefits<br>your business</h2>
  <div class="bcards">
    <div class="bcard"><div class="ring"><svg width="46" height="46" viewBox="0 0 46 46" fill="none" stroke="#1a76cc" stroke-width="2.5"><rect x="8" y="10" width="22" height="26"/><path d="M13 18h12M13 24h12M13 30h8"/><circle cx="34" cy="30" r="6"/></svg></div><h3>YOU COULD BE PAYING<br>TOO MUCH</h3><p>Public cloud pricing structures have a habit of sneakily scaling up very quickly. With NCAAS, you'll always know what you're paying for your private cloud services</p></div>
    <div class="bcard"><div class="ring"><svg width="46" height="46" viewBox="0 0 46 46" fill="none" stroke="#1a76cc" stroke-width="2.5"><circle cx="23" cy="16" r="8"/><path d="M6 34c6 0 10-4 16-4h10M6 38h28l6-6"/></svg></div><h3>YOU'RE LIKELY NOT GETTING<br>THE BENEFITS</h3><p>Public cloud providers cannot adopt new innovations and functions as quickly and easily as the private cloud solutions you'll get from NCAAS</p></div>
    <div class="bcard"><div class="ring"><svg width="46" height="46" viewBox="0 0 46 46" fill="none" stroke="#1a76cc" stroke-width="2.5"><circle cx="14" cy="14" r="4"/><circle cx="23" cy="12" r="4"/><circle cx="32" cy="14" r="4"/><path d="M10 36a13 11 0 0 1 26 0z"/></svg></div><h3>YOU'LL BE TIED TO THE SERVICES<br>YOUR PROVIDER CAN PROVIDE</h3><p>Public cloud providers will have a limited suite of products and services to offer you. A NCAAS private cloud has no such limitations</p></div>
  </div>
</section>

<section class="contact">
  <h2 class="title">Contact Us</h2>
  <div class="info" style="left:202px"><div class="pin"><svg width="28" height="28" viewBox="0 0 28 28" fill="none" stroke="#1a76cc" stroke-width="2.5"><path d="M14 25s-8-8-8-14a8 8 0 0 1 16 0c0 6-8 14-8 14z"/><circle cx="14" cy="11" r="3"/></svg></div><div><h4>LOCATION:</h4><p>465, Lorum Ipsum Dolore,<br>United States</p></div></div>
  <div class="info" style="left:508px;top:160px"><div class="pin"><svg width="28" height="28" viewBox="0 0 28 28" fill="none" stroke="#1a76cc" stroke-width="2.5"><path d="M7 4l5 1 1 5-3 2a14 14 0 0 0 6 6l2-3 5 1 1 5c-10 2-20-8-17-17z"/></svg></div><div><h4>CALL US:</h4><p>+1 (888) 888 8888</p></div></div>
  <div class="info" style="left:756px;top:157px"><div class="pin"><svg width="28" height="28" viewBox="0 0 28 28" fill="none" stroke="#1a76cc" stroke-width="2.5"><rect x="4" y="7" width="20" height="14"/><path d="M4 7l10 8 10-8"/></svg></div><div><h4>EMAIL US:</h4><p>info@nubelocloud.com</p></div></div>
  <div class="field" style="top:244px;left:165px;width:284px">Full Name</div>
  <div class="field" style="top:244px;left:458px;width:284px">Phone</div>
  <div class="field" style="top:244px;left:751px;width:284px">Email Address</div>
  <div class="field" style="top:304px;left:165px;width:870px;height:92px">Message</div>
  <span class="btn btn-blue send">SEND MESSAGE</span>
</section>

<footer class="footer">
  <div class="brand"><i></i><em>NubeloCloud</em></div>
  <div class="fnav">HOME<span>|</span>ABOUT US<span>|</span>PRODUCTS<span>|</span>SOLUTIONS<span>|</span>RESOURCES<span>|</span>CONTACT US</div>
  <div class="fcontact"><span style="color:#4aa3ff">&#9742;</span> +1 (888) 888 8888 &nbsp; | &nbsp; <span style="color:#4aa3ff">&#9993;</span> info@nubelocloud.com</div>
  <div class="fsocial"><span></span><span></span><span></span><span></span></div>
  <div class="copy">© 2022 NubeloCloud &nbsp;/&nbsp; All Rights Reserved</div>
</footer>

</body>
</html>
```